Tarvel Ridge LLC

Need Professional Business cards for New Investment Fund

Target Market(s)

High Quality investors

Industry/Entity Type

Financial

Contact Information for Business Card

Phone Number +1 555 284 6193
Name Pavel Orlinsky
Title Fund Manager
email po@FundTarvel.example
Website www.FundTarvel.example

Colors

Designer to choose colors to be used in the design.

Requirements
Must have
• Must have our Logo and all of the above. Must be made so lettering and loge can be raised

```html
<!DOCTYPE html>
<html lang="en">
<head>
<meta charset="utf-8">
<title>Tarvel Ridge LLC – Business Card</title>
<link href="https://fonts.googleapis.com/css2?family=Montserrat:wght@300;400;700&display=swap" rel="stylesheet">
<style>
  :root {
    --paper: #ffffff;
    --leaf: #5bbb4a;
    --forest: #434d42;
    --ink-light: #ffffff;
  }
  html, body {
    margin: 0;
    padding: 0;
    width: 1200px;
    height: 720px;
    overflow: hidden;
    background: var(--paper);
  }
  .card {
    position: relative;
    width: 1200px;
    height: 720px;
    background: var(--paper);
    font-family: "Montserrat", "Century Gothic", sans-serif;
    overflow: hidden;
  }
  .card-backdrop {
    position: absolute;
    inset: 0;
    width: 1200px;
    height: 720px;
  }
  .backdrop-top { fill: var(--leaf); }
  .backdrop-bottom { fill: var(--forest); }

  .brand {
    position: absolute;
    left: 150px;
    top: 430px;
    display: flex;
    align-items: center;
    gap: 14px;
  }
  .brand-mark {
    width: 22px;
    height: 22px;
    background: var(--leaf);
  }
  .brand-name {
    margin: 0;
    font-weight: 700;
    font-size: 34px;
    letter-spacing: 0.5px;
    color: var(--forest);
  }

  .person {
    position: absolute;
    left: 620px;
    top: 158px;
    color: var(--ink-light);
  }
  .person-name {
    margin: 0;
    font-weight: 700;
    font-size: 40px;
    line-height: 1.1;
    letter-spacing: 0.3px;
  }
  .person-title {
    margin: 4px 0 0;
    font-weight: 300;
    font-size: 31px;
    line-height: 1.2;
  }

  .contact-list {
    position: absolute;
    left: 618px;
    top: 463px;
    margin: 0;
    padding: 0;
    list-style: none;
    color: var(--ink-light);
  }
  .contact-item {
    display: flex;
    align-items: center;
    height: 43px;
    font-weight: 400;
    font-size: 31px;
    letter-spacing: 0.3px;
  }
  .contact-icon {
    width: 26px;
    height: 26px;
    margin-right: 22px;
    flex: none;
  }
  .contact-icon .solid { fill: var(--ink-light); }
  .contact-icon .stroke { fill: none; stroke: var(--ink-light); stroke-width: 2; }
</style>
</head>
<body>
<main class="card">
  <svg class="card-backdrop" viewBox="0 0 1200 720" aria-hidden="true">
    <polygon class="backdrop-top" points="279,0 1200,0 1200,358 653,358"/>
    <polygon class="backdrop-bottom" points="653,358 1200,358 1200,720 279,720"/>
  </svg>

  <div class="brand">
    <span class="brand-mark" aria-hidden="true"></span>
    <p class="brand-name">Tarvel Ridge</p>
  </div>

  <header class="person">
    <h1 class="person-name">Pavel Orlinsky</h1>
    <p class="person-title">Fund Manager</p>
  </header>

  <ul class="contact-list">
    <li class="contact-item">
      <svg class="contact-icon" viewBox="0 0 24 24" aria-hidden="true">
        <path class="solid" d="M6.6 2.5l3 3.6-1.8 2.2c1.3 2.8 3.4 4.9 6.2 6.2l2.2-1.8 3.6 3-1.9 3.3C11 18.5 5.5 13 4.3 4.4z"/>
      </svg>
      <span>+1 555 284 6193</span>
    </li>
    <li class="contact-item">
      <svg class="contact-icon" viewBox="0 0 24 24" aria-hidden="true">
        <path class="solid" d="M2 10l10-7 10 7v10H2z"/>
        <path d="M2 10l10 6 10-6" fill="none" stroke="#434d42" stroke-width="1.6"/>
      </svg>
      <span>po@FundTarvel.example</span>
    </li>
    <li class="contact-item">
      <svg class="contact-icon" viewBox="0 0 24 24" aria-hidden="true">
        <circle class="stroke" cx="12" cy="12" r="10"/>
        <ellipse class="stroke" cx="12" cy="12" rx="4.5" ry="10"/>
        <line class="stroke" x1="2" y1="12" x2="22" y2="12"/>
        <line class="stroke" x1="4" y1="7" x2="20" y2="7"/>
        <line class="stroke" x1="4" y1="17" x2="20" y2="17"/>
      </svg>
      <span>www.FundTarvel.example</span>
    </li>
  </ul>
</main>
</body>
</html>
```